Need Eye Catching For Sale By Owner Signs

In need of a Eye Catching For Sale By Owner Sign design. I plan on using the sign to market buildings and raw land that I own. The design should be able to scale to different rectangular dimensions for example a yard stake sign or a large 4' x 6' sign to be tacked to plywood. The design should have a dead space near the bottom that I can insert more detail information into at a later time.

The main tag line "For Sale By Owner" and the contact number "319-562-4097" needs to be easily be read from a distance.

```html
<!DOCTYPE html>
<html lang="en">
<head>
<meta charset="utf-8">
<title>For Sale By Owner Sign</title>
<link href="https://fonts.googleapis.com/css2?family=Arimo:wght@400&display=swap" rel="stylesheet">
<style>
  :root {
    --sign-red: #ed1c24;
    --sign-red-dark: #b3141a;
    --sign-white: #ffffff;
    --ink: #111111;
    --shadow: rgba(0, 0, 0, 0.22);
  }
  html, body {
    margin: 0;
    padding: 0;
    overflow: hidden;
    background: var(--sign-white);
  }
  .sign {
    position: relative;
    width: 1200px;
    height: 800px;
    overflow: hidden;
    background: var(--sign-white);
    font-family: "Arimo", Helvetica, Arial, sans-serif;
  }
  .tag-card {
    position: absolute;
    left: 313px;
    top: 67px;
    width: 840px;
    height: 373px;
    border-radius: 14px;
    background: var(--sign-white);
    box-shadow: 0 4px 8px var(--shadow);
  }
  .tag-art {
    position: absolute;
    left: 0;
    top: 67px;
    width: 387px;
    height: 373px;
    background: linear-gradient(to right, rgba(237, 28, 36, 0.15) 0, var(--sign-red) 150px, var(--sign-red) 100%);
  }
  .tagline {
    position: absolute;
    left: 462px;
    top: 111px;
    margin: 0;
    color: var(--sign-red);
    font-weight: 400;
    font-size: 142px;
    line-height: 133px;
    letter-spacing: 0;
  }
  .phone {
    position: absolute;
    left: 0;
    right: 0;
    top: 479px;
    margin: 0;
    text-align: center;
    color: var(--ink);
    font-size: 152px;
    line-height: 150px;
    font-weight: 400;
    letter-spacing: 0;
  }
  .info-band {
    position: absolute;
    left: 0;
    bottom: 0;
    width: 1200px;
    height: 118px;
    box-sizing: border-box;
    padding-bottom: 10px;
    background: linear-gradient(to bottom, var(--sign-red-dark) 0, var(--sign-red) 14px, var(--sign-red) 100%);
    box-shadow: 0 -3px 8px var(--shadow);
    display: flex;
    align-items: center;
    justify-content: center;
  }
  .info-text {
    margin: 0;
    color: var(--sign-white);
    font-size: 33px;
    white-space: nowrap;
  }
</style>
</head>
<body>
  <main class="sign">
    <div class="tag-card"></div>
    <div class="tag-art" role="img" aria-label="Red price tag end with an eyelet and a hanging grey string"></div>

    <h1 class="tagline">For Sale<br>By Owner</h1>

    <p class="phone">(319) 562 - 4097</p>

    <footer class="info-band">
      <p class="info-text">More information goes here - More information goes here - more information</p>
    </footer>
  </main>
</body>
</html>
```